Logo & Stationery Design for Non profit

This is  a nonprofit organization created to help minorities and seniors achieve financial freedom.  We want a logo that symbolizes hope and prosperity. 

Industry/Entity Type

Non Profit

Logo Text

Bright Harbor Foundation

Requirements
Must have
• The name "Bright Harbor Foundation"

```html
<!DOCTYPE html>
<html lang="en">
<head>
<meta charset="utf-8">
<title>Bright Harbor Foundation – Business Card</title>
<link href="https://fonts.googleapis.com/css2?family=Questrial&family=Arimo&family=Lato:wght@400&display=swap" rel="stylesheet">
<style>
  :root {
    --backdrop: #000000;
    --card: #ffffff;
    --ink: #4a4a4a;
    --gold: #ffc000;
  }
  html, body {
    margin: 0;
    padding: 0;
    width: 1086px;
    height: 1200px;
    overflow: hidden;
    background: var(--backdrop);
  }
  .canvas {
    position: relative;
    width: 1086px;
    height: 1200px;
  }
  .card {
    position: absolute;
    left: 15px;
    width: 1055px;
    height: 567px;
    background: var(--card);
    border-radius: 32px;
    overflow: hidden;
  }
  .card--front { top: 16px; }
  .card--back { top: 617px; }

  .brand-mark {
    position: absolute;
    border-radius: 50%;
    background: var(--gold);
  }
  .brand-name {
    position: absolute;
    margin: 0;
    font-family: "Questrial", sans-serif;
    font-weight: 400;
    color: var(--ink);
    white-space: nowrap;
  }

  .card--front .brand-mark { left: 161px; top: 76px; width: 206px; height: 206px; }
  .card--front .brand-name { left: 398px; top: 118px; font-size: 66px; line-height: 1.1; }
  .card--front .brand-name span { display: block; font-size: 28px; letter-spacing: 5px; text-align: right; line-height: 1.3; }

  .card--back .brand-mark { left: 71px; top: 51px; width: 66px; height: 66px; }
  .card--back .brand-name { left: 136px; top: 63px; font-size: 32px; letter-spacing: -0.5px; }

  .contact {
    position: absolute;
    left: 84px;
    margin: 0;
    font-family: "Arimo", sans-serif;
    font-size: 34px;
    line-height: 48px;
    color: var(--ink);
  }
  .card--front .contact { top: 354px; }
  .card--back .contact { top: 371px; }

  .person {
    position: absolute;
    left: 0;
    width: 100%;
    text-align: center;
  }
  .person__name {
    margin: 0;
    position: absolute;
    left: 0; right: 0;
    top: 155px;
    font-family: "Lato", sans-serif;
    font-weight: 400;
    font-size: 92px;
    color: var(--ink);
    line-height: 1;
  }
  .person__role {
    margin: 0;
    position: absolute;
    left: 0; right: 0;
    top: 290px;
    font-family: "Lato", sans-serif;
    font-size: 31px;
    color: var(--gold);
    line-height: 1;
  }
</style>
</head>
<body>
<main class="canvas">
  <section class="card card--front">
    <div class="brand-mark" aria-hidden="true"></div>
    <p class="brand-name">Bright Harbor<span>Foundation</span></p>
    <p class="contact">
      RIVERTON, IL<br>
      info@brightharbor.org &nbsp;/&nbsp; (000) 000-0000<br>
      www.brightharbor.org
    </p>
  </section>

  <section class="card card--back">
    <div class="brand-mark" aria-hidden="true"></div>
    <p class="brand-name">Bright Harbor Foundation</p>
    <div class="person">
      <h1 class="person__name">Daniel Reyes</h1>
      <p class="person__role">Chief executive officer</p>
    </div>
    <p class="contact">
      direct: 000-000-0000<br>
      address: RIVERTON, IL<br>
      email: dreyes@brightharbor.org
    </p>
  </section>
</main>
</body>
</html>
```